Fabric Softener

We need fabric softener. Bottle picture attached for reference. Color of bottle can be proposed as well. Normally bottle is pink and blue color

Logo is also attached that shall be used.
Updates

Need extra days to review

Low designer entries

Target Market(s)

Niche

Font styles to use
Sans Serif

Requirements
Must have
• Fabric, Brightness, Nature
Nice to have
• Good colors
Should not have
• Adults

```html
<!DOCTYPE html>
<html lang="en">
<head>
<meta charset="utf-8">
<title>Fabric Softener Labels</title>
<link rel="stylesheet" href="https://fonts.googleapis.com/css2?family=Asap:ital,wght@1,700&family=Kalam&family=Nunito:wght@600;800&family=Roboto+Condensed:wght@700&display=swap">
<style>
  :root {
    --stage: #f1eff8;
    --lav-deep: #4a2a8c;
    --lav-mid: #6a4fb0;
    --lav-light: #e9e1f7;
    --lav-sky: #c9b8ee;
    --lav-flower: #8a62c8;
    --sky-deep: #2f5fa6;
    --sky-mid: #4d86c8;
    --sky-light: #eaf3fd;
    --sky-soft: #b9d6f3;
    --sky-flower: #dbe9f8;
    --pink-band: #e8356e;
    --yellow-band: #ffd21f;
    --red-num: #e23a1e;
    --ink: #1f1f2e;
    --white: #ffffff;
  }
  * { margin: 0; padding: 0; box-sizing: border-box; }
  html, body { width: 1200px; height: 800px; overflow: hidden; }
  body {
    background: var(--stage);
    display: flex; align-items: center; justify-content: center; gap: 60px;
    font-family: "Nunito", sans-serif;
  }
  .label {
    position: relative; width: 500px; height: 680px; overflow: hidden;
    border-radius: 230px 230px 150px 150px / 200px 200px 120px 120px;
    box-shadow: 0 10px 30px rgba(60, 40, 120, .15);
  }
  .label--lavender { background: linear-gradient(160deg, var(--lav-sky), var(--lav-light) 55%, var(--white)); }
  .label--spring { background: linear-gradient(160deg, var(--sky-soft), var(--sky-light) 55%, var(--white)); }
  .floral { position: absolute; }
  .floral--side { left: 0; top: 120px; width: 120px; height: 470px; border-radius: 0 80px 80px 0; }
  .floral--corner { right: 0; bottom: 0; width: 200px; height: 180px; border-radius: 140px 0 0 0; }
  .label--lavender .floral--side { background: linear-gradient(180deg, var(--lav-flower), #b79be0 60%, #f3b3c9); }
  .label--lavender .floral--corner { background: linear-gradient(200deg, #f5a8bf, #fbe2a0 60%, var(--lav-light)); }
  .label--spring .floral--side { background: linear-gradient(180deg, var(--sky-flower), var(--white) 60%, #f4d36a); }
  .label--spring .floral--corner { background: linear-gradient(200deg, #f6b06a, #f7c4d0 60%, var(--sky-light)); }
  .tagline {
    position: absolute; top: 95px; right: 70px; text-align: right;
    font-family: "Kalam", cursive; font-size: 19px; line-height: 1.25; transform: rotate(-6deg);
  }
  .brand {
    position: absolute; top: 215px; left: 140px; right: 40px; text-align: center;
    font-family: "Nunito", sans-serif; font-weight: 800; font-size: 78px; letter-spacing: -1px;
  }
  .product {
    position: absolute; top: 395px; left: 120px; right: 20px; text-align: center;
  }
  .product__name { font-family: "Asap", sans-serif; font-style: italic; font-weight: 700; font-size: 44px; }
  .product__scent { font-weight: 600; font-size: 24px; letter-spacing: 1px; margin-top: 2px; }
  .loads {
    display: inline-flex; align-items: center; gap: 6px; margin-top: 16px; padding: 2px 18px;
    font-family: "Roboto Condensed", sans-serif; font-weight: 700;
  }
  .loads__count { font-size: 44px; line-height: 1; }
  .loads__unit { font-size: 16px; line-height: 1; text-align: left; }
  .label--lavender .loads { background: var(--pink-band); color: var(--white); }
  .label--spring .loads { background: var(--yellow-band); color: var(--red-num); }
  .net {
    position: absolute; top: 585px; left: 110px; right: 90px; text-align: center;
    font-family: "Roboto Condensed", sans-serif; font-weight: 700; color: var(--ink);
  }
  .net__volume { font-size: 22px; }
  .net__warning { font-size: 15px; }
  .label--lavender .tagline, .label--lavender .brand { color: var(--lav-deep); }
  .label--lavender .product__name { color: var(--lav-deep); }
  .label--lavender .product__scent { color: var(--lav-mid); }
  .label--spring .tagline, .label--spring .brand { color: var(--sky-deep); }
  .label--spring .product__name { color: var(--sky-deep); }
  .label--spring .product__scent { color: var(--sky-mid); }
</style>
</head>
<body>
  <section class="label label--lavender">
    <div class="floral floral--side" role="img" aria-label="Violet and lavender flowers"></div>
    <div class="floral floral--corner" role="img" aria-label="Pink and yellow blossoms"></div>
    <p class="tagline">Spring fresh<br>Bidegradable Formula</p>
    <h1 class="brand">Lumera</h1>
    <div class="product">
      <h2 class="product__name">Fabric Softener</h2>
      <p class="product__scent">LAVANDER FRESH</p>
      <div class="loads"><span class="loads__count">85</span><span class="loads__unit">SMALL<br>LOADS</span></div>
    </div>
    <div class="net">
      <p class="net__volume">NET 125 FL OZ. (3.7 L)</p>
      <p class="net__warning">KEEP OUT OF REACH OF CHILDREN</p>
    </div>
  </section>

  <section class="label label--spring">
    <div class="floral floral--side" role="img" aria-label="White blossoms and daisies"></div>
    <div class="floral floral--corner" role="img" aria-label="Orange and pink lilies"></div>
    <p class="tagline">Spring fresh<br>Bidegradable Formula</p>
    <h1 class="brand">Lumera</h1>
    <div class="product">
      <h2 class="product__name">Fabric Softener</h2>
      <p class="product__scent">LOREM IPSUM</p>
      <div class="loads"><span class="loads__count">85</span><span class="loads__unit">SMALL<br>LOADS</span></div>
    </div>
    <div class="net">
      <p class="net__volume">NET 125 FL OZ. (3.7 L)</p>
      <p class="net__warning">KEEP OUT OF REACH OF CHILDREN</p>
    </div>
  </section>
</body>
</html>
```